Website Design Required For Education Video Portfolio Site

I am looking for a designer to create a skin for a relaunch of my website - www.brightfieldlearningfilms.co.uk. We want a clean and stylish new design.

The website showcases prospectus/promotional videos that are made for schools and colleges. Videos will be hosted on video-sharing and embedded.

I want it to be stylish and clean.

I require 7 pages designed and this must be agreed in order to do the project.

1. Homepage
2. About
3. Prices
4. Testimonials
5. Contact Page with form
6. Promotional Videos
7. Subject Videos

The website will be then be built on the Wordpress system.

Target Market(s)

Education, Schools, Colleges, Universities

Industry/Entity Type

Education

Font styles to use
Serif

Colors

Designer to choose colors to be used in the design.

Requirements
Must have
• Video content, be clean, show our portfolio, descriptions about videos. I like the idea of having video headers.
Nice to have
• Images

```html
<!DOCTYPE html>
<html lang="en">
<head>
<meta charset="utf-8">
<title>Brightfield Learning Films – Home</title>
<link href="https://fonts.googleapis.com/css2?family=Poppins:wght@300;400;500;600;700&display=swap" rel="stylesheet">
<style>
:root{
  --blue:#1aa3e8;
  --navy:#283b8f;
  --deep:#0f2550;
  --beige:#f1eee9;
  --ink:#1b1b1b;
  --muted:#4a4a4a;
  --white:#ffffff;
}
*{box-sizing:border-box;margin:0;padding:0}
html,body{width:1200px;height:5146px;overflow:hidden}
body{font-family:'Poppins',sans-serif;color:var(--ink);background:var(--white);position:relative}
.abs{position:absolute}
.photo{position:absolute}
.btn{position:absolute;background:var(--blue);color:var(--white);font-size:11px;font-weight:700;letter-spacing:.5px;display:flex;align-items:center;justify-content:center;text-transform:uppercase}
.play{position:absolute;width:76px;height:76px;border-radius:50%;background:var(--blue);display:flex;align-items:center;justify-content:center}
.play.small{width:44px;height:44px}

/* hero */
.hero{position:absolute;left:0;top:0;width:1200px;height:572px;background:linear-gradient(100deg,#1d2228 0%,#3a4032 45%,#2a3a55 75%,#1a2230 100%)}
.brand{position:absolute;left:104px;top:22px;display:flex;align-items:center;gap:10px;color:var(--blue);font-weight:700;font-size:26px}
.brand .mark{width:36px;height:36px;border-radius:8px;background:var(--blue)}
.nav{position:absolute;right:100px;top:34px;display:flex;gap:30px;font-size:11px;color:var(--white);text-transform:uppercase;font-weight:500}
.nav .active{border-bottom:3px solid var(--blue);padding-bottom:20px}
.hero h1{position:absolute;left:104px;top:168px;font-size:52px;line-height:54px;font-weight:500;color:var(--white)}
.hero h1 .outline{color:transparent;-webkit-text-stroke:1.5px var(--blue);letter-spacing:2px}
.follow{position:absolute;left:1096px;top:210px;color:var(--white);font-size:10px;letter-spacing:2px;transform:rotate(-90deg);transform-origin:left top;font-weight:600}
.social{position:absolute;left:1102px;width:22px;height:22px;border-radius:50%;border:1.5px solid var(--white)}

/* intro */
.intro-bg{position:absolute;left:-300px;top:572px;width:1800px;height:1300px;background:var(--beige);border-radius:0 0 50% 50%/0 0 60% 60%}
.intro-title{position:absolute;left:106px;top:655px;width:460px;font-size:28px;line-height:40px;font-weight:400}
b,.strong{font-weight:600}
.intro-text{position:absolute;left:640px;top:655px;width:460px;font-size:14px;line-height:22px;color:var(--muted)}
.intro-text p+p{margin-top:18px}
.frame{position:absolute;left:176px;top:880px;width:846px;height:468px;background:var(--white)}
.cover{position:absolute;left:0;top:1350px;width:1200px;height:130px;background:var(--white)}

/* investment */
.h2{position:absolute;font-size:28px;line-height:40px;font-weight:400}
.body{position:absolute;font-size:14px;line-height:23px;color:var(--muted)}
.by{position:absolute;left:586px;top:1862px;width:510px;font-size:14px;line-height:22px;color:var(--muted)}
.by span{color:var(--blue);font-weight:700}

/* features */
.features{position:absolute;left:0;top:2076px;width:1200px;height:296px;background:var(--beige);border-top-right-radius:900px 120px}
.feature{position:absolute;top:62px;width:260px;font-size:13px;line-height:20px;color:var(--muted)}
.feature svg{display:block;margin-bottom:18px}

/* budget */
.budget{position:absolute;left:0;top:2372px;width:546px;height:500px;background:var(--navy)}
.budget h2{position:absolute;left:104px;top:80px;font-size:34px;line-height:46px;font-weight:500;color:var(--white)}
.budget p{position:absolute;left:104px;top:264px;width:380px;font-size:14px;line-height:23px;color:var(--white)}

/* videos */
.vids{position:absolute;left:0;top:3540px;width:1200px;height:420px;background:var(--beige);border-top-left-radius:900px 120px}
.card{position:absolute;top:40px;width:308px}
.thumb{width:308px;height:216px;position:relative;display:flex;align-items:center;justify-content:center}
.card .cat{margin-top:18px;font-size:12px;color:var(--blue);font-weight:500}
.card .title{margin-top:10px;font-size:14px;line-height:21px;font-weight:600}

/* drone */
.drone{position:absolute;left:0;top:3960px;width:1200px;height:502px;background:linear-gradient(180deg,#1c3e72 0%,#3f6fa8 45%,#123766 100%);text-align:center;color:var(--white)}
.drone .kicker{position:absolute;left:0;right:0;top:225px;font-size:13px;font-weight:600;letter-spacing:.5px}
.drone h2{position:absolute;left:0;right:0;top:262px;font-size:40px;line-height:54px;font-weight:400}
.drone h2 span{color:var(--blue)}

/* partners */
.partners-title{position:absolute;left:0;right:0;top:4524px;text-align:center;font-size:13px;font-weight:700;letter-spacing:.5px}
.partners{position:absolute;left:64px;top:4580px;width:1050px;height:104px;display:flex;border:1px solid #e6e6e6}
.partners div{flex:1;border-right:1px solid #e6e6e6;display:flex;align-items:center;justify-content:center}
.partners div:last-child{border-right:none}
.partners span{width:48px;height:48px;border-radius:50%;background:#d9dee8}

/* footer */
.footer{position:absolute;left:0;top:4740px;width:1200px;height:406px;background:var(--deep);color:var(--white)}
.footer h4{position:absolute;font-size:14px;font-weight:700;letter-spacing:1px}
.flinks{position:absolute;font-size:12px;line-height:30px;color:#c8d0e0}
.contact{position:absolute;left:764px;font-size:12px;font-weight:500;display:flex;gap:14px;line-height:18px}
.footer .rule{position:absolute;left:126px;top:326px;width:940px;height:1px;background:#3a4c74}
.ficon{position:absolute;top:314px;width:24px;height:24px;border-radius:50%;border:1.5px solid var(--white);background:var(--deep)}
.copy{position:absolute;left:0;right:0;top:366px;text-align:center;font-size:13px;color:#c8d0e0}
</style>
</head>
<body>

<section class="hero">
  <div class="photo" style="inset:0" role="img" aria-label="Pupils in school uniform gathered in a playground"></div>
  <div class="brand"><span class="mark"></span>Brightfield</div>
  <nav class="nav">
    <span class="active">Home</span><span>About</span><span>Promotional Videos</span><span>Subject Videos</span><span>Prices</span><span>Testimonials</span><span>Contact</span>
  </nav>
  <h1>We Make<br>Awesome<br>Educational<br><span class="outline">VIDEOS</span></h1>
  <div class="btn" style="left:104px;top:422px;width:146px;height:44px">Get Started</div>
  <div class="follow" style="top:296px">FOLLOW US</div>
  <div class="social" style="top:322px"></div>
  <div class="social" style="top:357px"></div>
  <div class="social" style="top:393px"></div>
</section>

<div class="intro-bg"></div>
<div class="cover"></div>
<h2 class="intro-title">Creating Bespoke <b>Education Videos</b> To Showcase Schools, Colleges &amp; Training Providers In <b>The North Of England</b></h2>
<div class="intro-text">
  <p>Here at Brightfield Learning Films, we know how to create stylish, engaging, and successful educational videos for schools, colleges and training providers. We’ve been making them for years.</p>
  <p>We believe that when you’re trying to attract new learners the best way to show how your learning establishment is better than the rest is with a compelling, top-quality video.</p>
</div>
<div class="frame">
  <div class="photo" style="left:10px;top:10px;width:826px;height:448px;background:linear-gradient(180deg,#7a8a6a 0%,#4f7d2f 45%,#3d6a22 100%)" role="img" aria-label="Children playing with a parachute on a school field"></div>
  <div class="play" style="left:385px;top:202px"><svg width="24" height="26" viewBox="0 0 24 26"><path d="M3 2l19 11L3 24z" fill="#fff"/></svg></div>
</div>

<h2 class="h2" style="left:106px;top:1506px;width:420px">A One-Off Investment That Brings <b>Long-Term Results</b></h2>
<p class="body" style="left:106px;top:1610px;width:384px">There are so many ways to repurpose your videos and make the initial investment work for you – sharing snippets on social media, embedding the video onto your website, uploading it to your video-sharing channel or playing it on your welcome screen in reception. The return on investment is excellent (and in some cases, instant!)</p>
<div class="photo" style="left:586px;top:1492px;width:508px;height:334px;background:radial-gradient(circle at 50% 50%,#3c4f7a 0%,#6c6f78 45%,#a99c8c 100%)" role="img" aria-label="A pupil crawling through a play tunnel"></div>
<div class="photo" style="left:0;top:1838px;width:504px;height:238px;background:linear-gradient(90deg,#b9a98e 0%,#9c6a4e 50%,#c9b8a0 100%)" role="img" aria-label="A pupil with a helmet riding a bike outside a school building"></div>
<p class="by"><span>BY THE WAY:</span> don’t just take our word for how successful our videos are. Check out some of the wonderful feedback we’ve received.</p>
<div class="btn" style="left:586px;top:1930px;width:202px;height:44px">Read Our Feedback</div>

<section class="features">
  <div class="feature" style="left:120px">
    <svg width="66" height="58" viewBox="0 0 66 58" fill="none" stroke="#1aa3e8" stroke-width="2"><circle cx="38" cy="29" r="24"/><path d="M32 19l16 10-16 10z"/><path d="M4 20h14M8 29h12M4 38h14"/></svg>
    We’re a smart bunch of experienced video makers and we know how to create compelling videos that get results.
  </div>
  <div class="feature" style="left:468px">
    <svg width="60" height="58" viewBox="0 0 60 58" fill="none" stroke="#1aa3e8" stroke-width="2"><path d="M10 20h12a5 5 0 1 1 10 0h12v12a5 5 0 1 1 0 10v12H10V42a5 5 0 1 0 0-10z"/></svg>
    We offer a cost-effective marketing solution – no more expensive brochure designing, printing and storage hassles. A video beats traditional marketing materials hands down.
  </div>
  <div class="feature" style="left:802px">
    <svg width="58" height="58" viewBox="0 0 58 58" fill="none" stroke="#1aa3e8" stroke-width="2"><circle cx="29" cy="31" r="22"/><path d="M20 31l7 7 13-14M29 4v5M10 10l4 4M48 10l-4 4"/></svg>
    We save you time and effort – you could invest time, effort and tech into making your own videos, but would they have the same polished, professional impact as ours?
  </div>
</section>

<section class="budget">
  <h2>Our Videos Won’t Eat Up All Of Your Marketing Budget Either!</h2>
  <p>You see we do things differently at Brightfield Learning Films. Our highly experienced and dedicated team is small (but mighty) and that’s how we keep costs low and affordable.</p>
  <div class="btn" style="left:104px;top:382px;width:176px;height:44px">View Our Prices</div>
</section>
<div class="photo" style="left:546px;top:2372px;width:654px;height:500px;background:linear-gradient(120deg,#2f6a5a 0%,#7aa0b0 50%,#2e7a55 100%)" role="img" aria-label="Pupils building a tower from construction blocks"></div>

<div class="photo" style="left:0;top:3000px;width:544px;height:540px;background:linear-gradient(135deg,#3c7a8c 0%,#6aa0b8 40%,#c97a4a 70%,#5a8aa0 100%)" role="img" aria-label="Two young pupils holding colourful ribbons"></div>
<h2 class="h2" style="left:640px;top:3006px;width:480px;font-size:31px;line-height:45px;font-weight:500">Creating Customised Educational Videos That Exceed Your Expectations</h2>
<p class="body" style="left:640px;top:3166px;width:460px">Prefer a prospectus video over a music-driven one? No problem. In fact, we can almost always cater for your specific needs and budgets. All you have to do is ask.</p>
<p class="body" style="left:640px;top:3250px;width:460px">Our mission is to capture the heart and soul of your school, college, training company, so your potential recruits can’t resist taking that next step towards enrolling.</p>
<p class="body" style="left:640px;top:3346px;color:var(--ink)">Take a look at our range of video offerings</p>
<div class="btn" style="left:640px;top:3408px;width:196px;height:44px">Watch Our Videos</div>

<section class="vids">
  <div class="card" style="left:120px">
    <div class="thumb" style="background:linear-gradient(135deg,#6b7a88,#3a4a66)" role="img" aria-label="Pupils beside a school welcome sign"><div class="play small"><svg width="14" height="16" viewBox="0 0 14 16"><path d="M2 1l11 7-11 7z" fill="#fff"/></svg></div></div>
    <div class="cat">Brightfield Learning Films</div>
    <div class="title">Hollins Green Primary School – Prospectus Video</div>
  </div>
  <div class="card" style="left:446px">
    <div class="thumb" style="background:linear-gradient(135deg,#7a8270,#4a5a6a)" role="img" aria-label="Aerial view of a school and surrounding streets"><div class="play small"><svg width="14" height="16" viewBox="0 0 14 16"><path d="M2 1l11 7-11 7z" fill="#fff"/></svg></div></div>
    <div class="cat">Brightfield Learning Films</div>
    <div class="title">Ashby Moor Primary School – Early Years Prospectus Video</div>
  </div>
  <div class="card" style="left:770px">
    <div class="thumb" style="background:linear-gradient(135deg,#8a9aa8,#3f6a4a)" role="img" aria-label="Pupils on a playground climbing frame"><div class="play small"><svg width="14" height="16" viewBox="0 0 14 16"><path d="M2 1l11 7-11 7z" fill="#fff"/></svg></div></div>
    <div class="cat">Brightfield Learning Films</div>
    <div class="title">2022-03-11 – Kirkwell St Anne’s – Promo</div>
  </div>
</section>

<section class="drone" role="img" aria-label="A camera drone flying against a blue sky">
  <div class="kicker">LICENSED BY THE NATIONAL AIRSPACE BOARD</div>
  <h2>We Are <span>Licensed Drone Operators</span> Meaning<br>We Can Take To The Sky.</h2>
</section>

<div class="partners-title">SCHOOLS, COLLEGES AND TRAINING PROVIDERS WE’VE WORKED WITH</div>
<div class="partners">
  <div><span></span></div><div><span></span></div><div><span></span></div><div><span></span></div><div><span></span></div>
  <div><span></span></div><div><span></span></div><div><span></span></div><div><span></span></div><div><span></span></div>
</div>

<footer class="footer">
  <h4 style="left:126px;top:94px">USEFUL LINKS</h4>
  <div class="flinks" style="left:126px;top:136px">Home<br>About Us<br>Promotional Video<br>Subject Video</div>
  <div class="flinks" style="left:308px;top:138px">Prices<br>Testimonials<br>Contact</div>
  <div class="brand" style="left:494px;top:70px;font-size:28px"><span class="mark"></span>Brightfield</div>
  <h4 style="left:0;right:0;top:150px;text-align:center">OUR MISSION</h4>
  <p class="flinks" style="left:480px;top:196px;width:240px;text-align:center;font-size:11px;line-height:18px">Striving to deliver quality video content for schools and colleges in the North of England.</p>
  <h4 style="left:764px;top:96px">CONTACT US</h4>
  <div class="contact" style="top:140px"><svg width="14" height="18" viewBox="0 0 14 18"><path d="M7 1a6 6 0 0 1 6 6c0 4-6 10-6 10S1 11 1 7a6 6 0 0 1 6-6z" fill="#1aa3e8"/><circle cx="7" cy="7" r="2" fill="#0f2550"/></svg><span>Unit 4, Calder Works, Oakridge,<br>Durham. DH1 4XY.</span></div>
  <div class="contact" style="top:196px"><svg width="14" height="14" viewBox="0 0 14 14"><path d="M3 1l3 3-2 2a8 8 0 0 0 4 4l2-2 3 3-2 2C6 13 1 8 1 3z" fill="#1aa3e8"/></svg><span>07700 900 318</span></div>
  <div class="contact" style="top:236px"><svg width="16" height="12" viewBox="0 0 16 12"><rect x="0" y="0" width="16" height="12" rx="1" fill="#1aa3e8"/><path d="M1 1l7 6 7-6" stroke="#0f2550" fill="none" stroke-width="1.5"/></svg><span>info@brightfieldlearningfilms.co.uk</span></div>
  <div class="rule"></div>
  <div class="ficon" style="left:550px"></div>
  <div class="ficon" style="left:586px"></div>
  <div class="ficon" style="left:622px"></div>
  <div class="copy">© 2023 All Rights Reserved | Brightfield Learning Films</div>
</footer>

</body>
</html>
```